VELNA BROCADE

Project name: “Velna Brocade” website
Objective: To create an elegant website,
intuitive and responsive to present this
what is “Velna Brocade”
See attached specifications.

```html
<!DOCTYPE html>
<html lang="fr">
<head>
<meta charset="UTF-8">
<title>Velna Brocade</title>
<link href="https://fonts.googleapis.com/css2?family=Outfit:wght@400;500;600&family=Montserrat:ital,wght@0,400;0,500;0,600;1,400&display=swap" rel="stylesheet">
<style>
:root{
  --green:#3b5538;
  --green-dark:#2f452d;
  --mint:#c7dfcc;
  --mint-soft:#dfeee3;
  --grey:#f1f1f1;
  --text:#4a4a4a;
  --white:#ffffff;
  --star:#e59a2c;
}
*{margin:0;padding:0;box-sizing:border-box}
html,body{width:1200px;height:4112px;overflow:hidden}
body{position:relative;background:var(--white);font-family:'Montserrat',sans-serif;color:var(--text)}
.abs{position:absolute}
h1,h2,h3,.brand{font-family:'Outfit',sans-serif}
.btn{position:absolute;display:flex;align-items:center;justify-content:center;border-radius:40px;font-family:'Outfit',sans-serif;font-weight:500;font-size:14px;white-space:nowrap}
.btn-dark{background:var(--green);color:var(--white)}
.btn-mint{background:var(--mint);color:var(--green)}

/* hero */
.hero-photo{left:0;top:0;width:1200px;height:846px;background:radial-gradient(circle at 62% 35%,#c9a7a9 0,#8a7a6c 18%,#2f4a2c 40%,#1e3320 75%)}
.hero-wave{left:0;top:600px}
.nav{left:75px;top:22px;width:1050px;height:101px;background:var(--white);border-radius:60px}
.nav-logo{left:22px;top:18px;display:flex;align-items:center;gap:14px}
.logo-dot{width:66px;height:66px;border-radius:50%;border:2px solid var(--green)}
.brand-name{font-family:'Outfit',sans-serif;font-weight:600;color:var(--green);font-size:17px;letter-spacing:2px}
.nav-links{left:420px;top:41px;display:flex;gap:26px;font-size:13px;color:#555}
.nav-links .sep{color:#777}
.nav-cta{left:823px;top:30px;width:201px;height:40px;font-size:13px}
.hero-title{left:75px;top:228px;font-size:72px;line-height:76px;font-weight:600;color:var(--white);letter-spacing:-1.5px}
.hero-sub{left:77px;top:460px;font-size:13px;color:var(--white)}
.hero-cta{left:77px;top:496px;width:199px;height:40px}

/* about */
.about-photo{left:151px;top:906px;width:400px;height:400px;border-radius:50%;background:var(--mint)}
.about-photo-inner{position:absolute;left:12px;top:0;width:388px;height:388px;border-radius:50%;background:linear-gradient(180deg,#e9eef2 0,#9aa58a 35%,#5d6b3c 55%,#b3a58c 72%,#6c6f62 100%)}
.about-title{left:603px;top:976px;font-size:36px;font-weight:500;color:var(--green)}
.about-text{left:603px;top:1030px;width:445px;font-size:11.5px;line-height:19px;color:#555}
.about-text p+p{margin-top:12px}
.about-cta{left:603px;top:1194px;width:147px;height:40px;font-size:13px}

/* actions */
.section-title{left:0;width:1200px;text-align:center;font-size:36px;font-weight:500;color:var(--green)}
.green-band{left:0;top:1700px}
.card{width:246px;height:283px;background:var(--white);border-radius:16px;box-shadow:0 6px 20px rgba(0,0,0,.08);overflow:hidden;text-align:center}
.card-img{height:168px}
.card h3{margin-top:16px;font-size:16px;font-weight:500;color:var(--green-dark)}
.card p{margin:8px auto 0;width:200px;font-size:10.5px;line-height:16px;color:#666}

/* activities */
.act-title{left:78px;top:1995px;font-size:36px;font-weight:500;color:var(--white)}
.act-text{left:78px;top:2050px;width:440px;font-size:11.5px;line-height:18px;color:#e6ece5}
.act-list{left:78px;top:2121px;list-style:none;font-size:11.5px;color:#e6ece5}
.act-list li{height:24px;position:relative;padding-left:19px}
.act-list li::before{content:"";position:absolute;left:0;top:5px;width:7px;height:7px;border-radius:50%;background:#e6ece5}
.act-cta{left:78px;top:2210px;width:216px;height:38px}
.circle-fade{left:845px;top:1902px;width:384px;height:384px;border-radius:50%;background:#5b7457}
.circle-big{left:660px;top:1875px;width:438px;height:438px;border-radius:50%;background:linear-gradient(160deg,#b8c3cc 0,#c59a72 45%,#8c5a36 80%,#4c3a2c 100%)}
.circle-small{left:563px;top:2119px;width:208px;height:208px;border-radius:50%;background:linear-gradient(160deg,#f0e2c6 0,#d77b2a 45%,#8b3d1c 100%)}

/* faq */
.faq-item{left:271px;width:658px;height:45px;background:var(--grey);border-radius:24px;display:flex;align-items:center;justify-content:space-between;padding:0 20px 0 38px;font-family:'Outfit',sans-serif;font-weight:500;font-size:15px;color:#333}
.faq-toggle{width:20px;height:20px;border-radius:50%;background:var(--green);display:flex;align-items:center;justify-content:center}

/* reviews */
.review{width:303px;height:169px;background:var(--white);border-radius:14px;box-shadow:0 6px 20px rgba(0,0,0,.07);padding:22px 22px}
.stars{color:var(--star);font-size:16px;letter-spacing:3px}
.review p{margin-top:8px;font-style:italic;font-size:11px;line-height:18px;color:#666}
.review .author{margin-top:8px;font-family:'Outfit',sans-serif;font-weight:500;font-size:12.5px;color:#333}
.dots{left:576px;top:3051px;display:flex;gap:7px}
.dots span{width:11px;height:11px;border-radius:50%;background:#c5c5c5}
.dots span.on{background:var(--green-dark)}

/* contact */
.contact{left:227px;top:3155px;width:747px;height:372px;background:var(--white);border-radius:22px;box-shadow:0 6px 28px rgba(0,0,0,.07)}
.field{position:absolute;background:var(--grey);border-radius:22px;font-size:11px;color:#888;padding:13px 24px}
.contact-cta{left:300px;top:302px;width:146px;height:38px;font-size:13px}

/* footer */
.footer-band{left:0;top:3560px}
.footer-logo{left:539px;top:3718px;width:122px;height:122px;border-radius:50%;border:3px solid var(--white)}
.footer-brand{left:0;top:3858px;width:1200px;text-align:center;font-family:'Outfit',sans-serif;font-weight:500;color:var(--white);font-size:27px;letter-spacing:4px}
.footer-links{left:0;top:3922px;width:1200px;display:flex;justify-content:center;gap:48px;font-size:13.5px;color:var(--white)}
.social{left:511px;top:3966px;display:flex;gap:8px}
.social span{width:38px;height:38px;border-radius:50%;background:#5a7157}
.social span:first-child{background:var(--mint)}
.footer-rule{left:75px;top:4055px;width:1050px;height:1px;background:#8aa087}
.copyright{left:0;top:4075px;width:1200px;text-align:center;font-size:11px;color:var(--white)}
</style>
</head>
<body>

<section class="hero">
  <div class="abs hero-photo" role="img" aria-label="Photo d'une femme souriante devant un feuillage verdoyant"></div>
  <svg class="abs hero-wave" width="1200" height="260" viewBox="0 600 1200 260">
    <path d="M0 690 C40 650 90 640 140 650 C300 690 380 850 560 846 C720 842 820 740 940 734 C1070 728 1140 780 1200 846 L1200 860 L0 860Z" fill="var(--mint)"/>
    <path d="M0 706 C40 668 90 660 140 668 C300 705 380 862 560 858 C720 852 820 756 940 752 C1070 748 1140 800 1200 860 L0 860Z" fill="var(--white)"/>
  </svg>

  <nav class="abs nav">
    <div class="abs nav-logo"><span class="logo-dot"></span><span class="brand-name">VELNA BROCADE</span></div>
    <div class="abs nav-links"><span>Accueil</span><span class="sep">|</span><span>Nos Actions</span><span class="sep">|</span><span>Activités</span><span class="sep">|</span><span>Contact</span></div>
    <div class="btn btn-dark nav-cta">Prendre Rendez-vous</div>
  </nav>

  <h1 class="abs hero-title">Découvrez le<br>Limousin, Votre<br>Nouveau</h1>
  <p class="abs hero-sub">Connectez-vous aux meilleurs terrains à bâtir avec Velna Brocade.</p>
  <div class="btn btn-mint hero-cta">Prendre Rendez-vous</div>
</section>

<section class="about">
  <div class="abs about-photo"><div class="about-photo-inner" role="img" aria-label="Photo d'un pont ancien en pierre se reflétant dans une rivière bordée d'arbres"></div></div>
  <h2 class="abs about-title">Qui sommes-nous ?</h2>
  <div class="abs about-text">
    <p>Velna Brocade facilite la mise en relation entre particuliers et vendeurs de terrains à bâtir. Nous accompagnons les familles, couples et professionnels pour découvrir et investir dans le Limousin, en toute simplicité.</p>
    <p>Notre mission est de rendre l’achat de terrains simple, sécurisé et agréable. Nous offrons un accompagnement personnalisé à chaque étape, du choix du terrain jusqu’à la signature finale, en mettant l’accent sur la qualité, la transparence et la satisfaction de nos clients.</p>
  </div>
  <div class="btn btn-dark about-cta">En savoir plus</div>
</section>

<svg class="abs green-band" width="1200" height="700" viewBox="0 1700 1200 700">
  <path d="M0 1745 C120 1850 250 1915 400 1912 C560 1908 680 1830 800 1770 C930 1708 1070 1700 1200 1716 L1200 2400 L0 2400Z" fill="var(--green)"/>
</svg>

<section class="actions">
  <h2 class="abs section-title" style="top:1388px">Nos Actions</h2>
  <div class="abs card" style="left:215px;top:1455px"><div class="card-img" role="img" aria-label="Photo d'un salon moderne avec fauteuils" style="background:linear-gradient(160deg,#4a3a2e,#b9a58f 60%,#d8d2c8)"></div><h3>Transformation digitale</h3><p>Nous modernisons le processus d’achat et de vente de terrains grâce à des outils numériques...</p></div>
  <div class="abs card" style="left:477px;top:1455px"><div class="card-img" role="img" aria-label="Photo de personnes en réunion autour d'une table" style="background:linear-gradient(160deg,#7d8790,#b0654a 55%,#3a3f4a)"></div><h3>Prospection foncière</h3><p>Nous aidons les familles et investisseurs à trouver les meilleurs terrains disponibles dans...</p></div>
  <div class="abs card" style="left:739px;top:1455px"><div class="card-img" role="img" aria-label="Photo d'un espace de travail aux assises vertes et orange" style="background:linear-gradient(160deg,#dfe3e2,#8fa593 50%,#d6882d 85%)"></div><h3>Autres initiatives</h3><p>Velna Brocade s’engage également dans des projets locaux pour dynamiser le territoire...</p></div>
</section>

<section class="act">
  <div class="abs circle-fade"></div>
  <div class="abs circle-big" role="img" aria-label="Photo d'une famille souriante en tenue d'hiver"></div>
  <div class="abs circle-small" role="img" aria-label="Photo d'une famille dans un parc aux feuilles d'automne"></div>
  <h2 class="abs act-title">Activités à Découvrir</h2>
  <p class="abs act-text">Horizontal card layout avec images cliquables pour chaque activité. Chaque carte montre un lieu ou une activité avec un titre et un lien pour plus de détails.</p>
  <ul class="abs act-list"><li>Randonnée dans les collines du Limousin.</li><li>Marché local du village.</li><li>Festival culturel du Limousin.</li></ul>
  <div class="btn btn-mint act-cta">Voir Toutes les Activités</div>
</section>

<section class="faq">
  <h2 class="abs section-title" style="top:2482px">Questions Fréquentes</h2>
  <div class="abs faq-item" style="top:2549px">Ex: “Comment prendre rendez-vous ?”<span class="faq-toggle"><svg width="8" height="6" viewBox="0 0 8 6"><path d="M1 1l3 3 3-3" stroke="#fff" stroke-width="1.4" fill="none"/></svg></span></div>
  <div class="abs faq-item" style="top:2603px">“Quels terrains sont disponibles ?”<span class="faq-toggle"><svg width="8" height="6" viewBox="0 0 8 6"><path d="M1 1l3 3 3-3" stroke="#fff" stroke-width="1.4" fill="none"/></svg></span></div>
  <div class="abs faq-item" style="top:2657px">“Comment obtenir des conseils pour l’achat ?”<span class="faq-toggle"><svg width="8" height="6" viewBox="0 0 8 6"><path d="M1 1l3 3 3-3" stroke="#fff" stroke-width="1.4" fill="none"/></svg></span></div>
</section>

<section class="reviews">
  <h2 class="abs section-title" style="top:2786px">Avis de Nos Clients</h2>
  <div class="abs review" style="left:126px;top:2852px"><div class="stars">★★★★★</div><p>Une équipe professionnelle et à l’écoute. Grâce à Velna Brocade, nous avons trouvé le terrain idéal pour construire notre maison.</p><div class="author">Claire &amp; Hugo M.</div></div>
  <div class="abs review" style="left:448px;top:2852px"><div class="stars">★★★★★</div><p>Service rapide, clair et très rassurant. Les conseils fournis ont vraiment fait la différence dans notre choix. Je recommande vivement</p><div class="author">Jean-Luc P.</div></div>
  <div class="abs review" style="left:771px;top:2852px"><div class="stars">★★★★★</div><p>Nous avons été impressionnés par la connaissance du territoire et la transparence de Velna Brocade. Merci pour votre aide dans</p><div class="author">Famille Moreau</div></div>
  <div class="abs dots"><span></span><span class="on"></span><span></span></div>
</section>

<section class="abs contact">
  <h2 class="abs section-title" style="left:0;width:747px;top:26px">Contactez-Nous</h2>
  <div class="field" style="left:27px;top:94px;width:340px;height:39px">Enter Your First Name...</div>
  <div class="field" style="left:379px;top:94px;width:339px;height:39px">Enter Your Last Name...</div>
  <div class="field" style="left:27px;top:147px;width:340px;height:39px">Enter Your Email Address...</div>
  <div class="field" style="left:379px;top:147px;width:339px;height:39px">Enter Your Phone Number...</div>
  <div class="field" style="left:27px;top:198px;width:691px;height:86px;border-radius:18px">Please Send Your Message...</div>
  <div class="btn btn-dark contact-cta">Submit Now</div>
</section>

<footer>
  <svg class="abs footer-band" width="1200" height="552" viewBox="0 3560 1200 552">
    <path d="M0 3840 C250 3640 500 3600 700 3610 C900 3620 1080 3700 1200 3800 L1200 4112 L0 4112Z" fill="var(--mint)"/>
    <path d="M0 3880 C250 3690 500 3640 700 3648 C900 3656 1080 3740 1200 3840 L1200 4112 L0 4112Z" fill="var(--green)"/>
  </svg>
  <div class="abs footer-logo"></div>
  <div class="abs footer-brand">VELNA BROCADE</div>
  <div class="abs footer-links"><span>Accueil</span><span>|</span><span>Nos Actions</span><span>|</span><span>Activités</span><span>|</span><span>Contact Us</span></div>
  <div class="abs social"><span></span><span></span><span></span><span></span></div>
  <div class="abs footer-rule"></div>
  <p class="abs copyright">© 2025 Velna Brocade. Tous droits réservés.</p>
</footer>

</body>
</html>
```